Brightfold Reach - B2B Demand Generation Website Project

We need a fully functional website for www.brightfoldreach-example.com. We are a B2B Demand Generation company, based in London, working with companies such as QTR, DWN, Vortan, Brelloway, Pelta generating them sales leads for their sales teams. We run this through digital marketing newsletter promotions and have a network of websites. Content syndication, data, demand generation, online marketing. Our logo has just been redone (attached) and we have a holding page already which i would like to use the style / colours. Our logo is bright and vibrant but i dont want the site to be a rainbow. We are expensive, classy, professorial, B2B, intelligent.

Home
About Us
Our Services
Prospero & QA Technology
Intent Data
Testimonials
Contact Us

Target Market(s)

B2B Marketers (QTR, Quorvane, Pelta, DWN, Vista Hub, Harrowby, Tremont Axis, Technology Companies, Data Companies, Marketing Teams, Cloudwick.

Industry/Entity Type

Marketing

Coding

Coded - Design and coding required

Number of Pages Required

5+ page

Font styles to use
Sans Serif

Requirements
Must have
• Home
About Us
Our Services
Prospero & QA Technology
Intent Data
Testimonials
Contact Us

Simple Pages.

Look classy, intelligent, data experts. I like the video homepages were the image moves at the top. Very soft animation.
Nice to have
• Websites i like:

https://www.dwn-example.com/
https://www.pulsegate-example.com/
https://www.lmsitecraft-example.co.uk/

Brightfold Reach - The Demand Generation Company
Should not have
• Pixelvault crap images

```html
<!DOCTYPE html>
<html lang="en">
<head>
<meta charset="utf-8">
<title>Brightfold Reach - The Demand Generation Company</title>
<link rel="stylesheet" href="https://fonts.googleapis.com/css2?family=Domine:wght@400;500&family=Poppins:ital,wght@0,400;0,500;0,600;0,700;1,400&display=swap">
<style>
:root{
  --red:#c0282d;
  --blue:#1f5fa6;
  --navy:#0f1d4e;
  --ink:#1b1b1b;
  --text:#3a3a3a;
  --grey-band:#e2e5ea;
  --white:#ffffff;
}
*{margin:0;padding:0;box-sizing:border-box}
html,body{width:1200px;height:4149px;overflow:hidden}
body{position:relative;font-family:"Poppins",sans-serif;color:var(--text);background:var(--white)}
.abs{position:absolute}
.serif{font-family:"Domine",serif;color:var(--ink);font-weight:400}

/* hero */
.hero-bg{left:0;top:0;width:1200px;height:630px;
  background:
   radial-gradient(ellipse 420px 360px at 80px 330px,rgba(190,30,40,.75),transparent 70%),
   radial-gradient(ellipse 520px 420px at 980px 320px,rgba(30,110,200,.55),transparent 70%),
   linear-gradient(100deg,#2a0b1a 0%,#0a1634 45%,#0a2a55 100%)}
.hero-strip{left:899px;top:630px;width:301px;height:66px;background:linear-gradient(180deg,#0a2a55,#0b2142)}
.logo-name{left:56px;top:86px;width:300px;text-align:center;font-size:30px;font-weight:400;color:var(--red);letter-spacing:-.5px;line-height:1;white-space:nowrap}
.logo-tag{left:56px;top:126px;width:300px;text-align:center;font-size:9px;color:var(--red);white-space:nowrap}
.nav{left:430px;top:58px;display:flex;gap:20px;font-size:12px;font-weight:500;color:var(--white);white-space:nowrap}
.nav span.active{color:#4c9be8;position:relative}
.nav span.active::after{content:"";position:absolute;left:0;right:0;top:26px;height:2px;background:#4c9be8}
.hero-title{left:151px;top:232px;font-size:66px;color:var(--white);white-space:nowrap}
.hero-sub{left:152px;top:330px;font-size:21px;font-weight:500;letter-spacing:4.2px;color:var(--white);white-space:nowrap}
.btn{display:flex;align-items:center;justify-content:center;font-size:11.5px;font-weight:600;letter-spacing:.5px;color:var(--white)}
.btn-red{left:156px;top:400px;width:181px;height:53px;background:var(--red)}
.btn-blue{background:var(--blue);width:140px;height:50px}

/* stats */
.stat{display:flex;gap:14px;align-items:center}
.stat small{display:block;font-size:11px;color:#444}
.stat b{display:block;font-size:16px;font-weight:600;color:#244a8c;margin-top:2px}
.b2b{left:926px;top:609px;width:124px;height:145px;background:var(--red);color:var(--white);padding:16px 18px}
.b2b p{font-size:13px;font-weight:600;line-height:1.25;margin-top:10px}

/* sections */
.h2{font-size:40px}
.para{font-size:13px;line-height:26.5px;color:#333}
.partners{left:122px;top:1343px;width:950px;display:flex;align-items:center;justify-content:space-between}
.partner{font-size:34px;font-weight:600;letter-spacing:1px}

.services-band{left:0;top:1524px;width:1200px;height:524px;background:var(--grey-band)}
.card{width:286px;height:343px;background:var(--white);padding:38px 24px 0;box-shadow:0 2px 8px rgba(0,0,0,.05)}
.card h3{font-family:"Domine",serif;font-weight:400;font-size:18px;line-height:27px;color:var(--blue);margin-top:26px}
.card p{font-size:11.5px;line-height:21px;color:#333;margin-top:18px;height:84px}
.card a{display:inline-block;margin-top:16px;font-size:11px;font-weight:700;color:var(--red);text-decoration:underline;text-underline-offset:3px}

.quote-name{left:0;top:3508px;width:1200px;text-align:center;font-family:"Domine",serif;font-size:19px;color:var(--blue)}
.quote{left:242px;top:3561px;width:716px;text-align:center;font-size:15.5px;font-style:italic;line-height:29px;color:#333}

/* footer */
.footer{left:0;top:3781px;width:1200px;height:368px;background:linear-gradient(180deg,#101c5c,#0a1447)}
.contact{display:flex;align-items:center;gap:26px;color:var(--white);white-space:nowrap}
.contact .ic{width:52px;height:52px;border-radius:50%;background:var(--white);display:flex;align-items:center;justify-content:center}
.contact small{display:block;font-size:13px;letter-spacing:2px;font-weight:500}
.contact b{display:block;font-weight:600}
.foot-nav{left:0;top:3980px;width:1200px;display:flex;justify-content:center;gap:20px;font-size:12px;color:var(--white)}
.copy{left:0;top:4006px;width:1200px;text-align:center;font-size:12px;color:var(--white)}
.social{left:0;top:4052px;width:1200px;display:flex;justify-content:center;gap:22px}
.social span{width:18px;height:18px;border-radius:50%;border:2px solid var(--white)}
</style>
</head>
<body>

<!-- Hero -->
<div class="abs hero-bg" role="img" aria-label="Dark network of glowing connected points, red on the left fading into blue"></div>
<div class="abs hero-strip"></div>
<div class="abs logo-name">Brightfold Reach</div>
<div class="abs logo-tag">The Demand Generation Company</div>
<nav class="abs nav">
  <span class="active">Home</span><span>About Us</span><span>Our Services</span><span>Prospero &amp; QA Technology</span><span>Intent Data</span><span>Testimonials</span><span>Contact Us</span>
</nav>
<h1 class="abs serif hero-title">Brightfold Reach</h1>
<div class="abs hero-sub">THE DEMAND GENERATION COMPANY</div>
<div class="abs btn btn-red">GET STARTED NOW</div>

<!-- Stats -->
<div class="abs stat" style="left:130px;top:654px">
  <svg width="42" height="40" viewBox="0 0 42 40" fill="none" stroke="#c0282d" stroke-width="2.2"><path d="M12 28H9a7 7 0 0 1 0-14 11 11 0 0 1 21-2 8 8 0 0 1 3 16h-3"/><path d="M21 17v18M15 29l6 6 6-6"/></svg>
  <div><small>Downloads Per Month</small><b>Ticker to 70,000+</b></div>
</div>
<div class="abs stat" style="left:380px;top:654px">
  <svg width="42" height="40" viewBox="0 0 42 40" fill="none" stroke="#c0282d" stroke-width="2.2"><path d="M3 18 38 4 30 36 20 24zM20 24l18-20M20 24v10l5-5"/></svg>
  <div><small>Leads Delivered Per Month</small><b>Ticker 25,000+</b></div>
</div>
<div class="abs stat" style="left:652px;top:654px">
  <svg width="40" height="40" viewBox="0 0 40 40" fill="none" stroke="#c0282d" stroke-width="2.2"><circle cx="20" cy="20" r="17"/><path d="M8 10c5 2 6 6 4 9s2 6 5 6-1 8-3 10M24 4c-2 4 2 6 5 6s5 4 3 7-5 2-6 6 2 6 4 8"/></svg>
  <div><small>Countries We Can Reach</small><b>Ticker to 50+</b></div>
</div>
<div class="abs b2b">
  <svg width="48" height="46" viewBox="0 0 48 46" fill="none" stroke="#fff" stroke-width="2"><rect x="3" y="3" width="16" height="12" rx="1"/><rect x="29" y="3" width="16" height="12" rx="1"/><circle cx="11" cy="27" r="4"/><circle cx="37" cy="27" r="4"/><path d="M3 43c0-6 4-9 8-9s8 3 8 9M29 43c0-6 4-9 8-9s8 3 8 9M21 9h6M24 6l3 3-3 3"/></svg>
  <p>B2B<br>Solutions</p>
  <svg width="20" height="10" viewBox="0 0 20 10" fill="none" stroke="#fff" stroke-width="1.6" style="margin-top:4px"><path d="M0 5h18M14 1l4 4-4 4"/></svg>
</div>

<!-- About -->
<div class="abs" style="left:150px;top:828px;width:446px;height:390px;background:linear-gradient(160deg,#5a6470,#2b3038 60%,#1c2026)" role="img" aria-label="Smiling businessman in a dark suit at a desk with a laptop in a modern office"></div>
<h2 class="abs serif h2" style="left:652px;top:820px">About Us</h2>
<p class="abs para" style="left:652px;top:898px;width:392px">Brightfold Reach offers multi-channel demand generation services to publishers and technology vendors through our network of lead generation websites and native speaking telemarketing agents. Whether looking for MQL, ABM or BANT campaigns, Brightfold Reach can assist you in delivering your demand generation strategy and generate pipeline for your sales teams and/or channel partners.</p>
<div class="abs btn btn-blue" style="left:656px;top:1137px">READ MORE</div>

<div class="abs" style="left:151px;top:1285px;font-size:26px;font-weight:500;color:var(--ink);letter-spacing:.5px;font-family:'Domine',serif">WHO WE WORK WITH:</div>
<div class="abs partners">
  <svg width="16" height="26" viewBox="0 0 16 26" fill="none" stroke="#333" stroke-width="2"><path d="M13 2 3 13l10 11"/></svg>
  <span class="partner" style="color:#1f70c1">QTR</span>
  <span class="partner" style="color:#1f8fd1">Pelta</span>
  <span class="partner" style="color:#1f70c1">Kestrel</span>
  <span class="partner" style="color:#1f9ad6">Cirrusly</span>
  <span class="partner" style="color:#e1251b">Orvane</span>
  <svg width="16" height="26" viewBox="0 0 16 26" fill="none" stroke="#333" stroke-width="2"><path d="M3 2l10 11L3 24"/></svg>
</div>

<!-- Services -->
<div class="abs services-band"></div>
<h2 class="abs serif" style="left:0;top:1572px;width:1200px;text-align:center;font-size:36px">Our Services</h2>
<div class="abs card" style="left:150px;top:1640px">
  <svg width="64" height="66" viewBox="0 0 64 66" fill="none" stroke="#c0282d" stroke-width="2"><circle cx="32" cy="26" r="18"/><circle cx="32" cy="26" r="12"/><path d="M20 40 12 60l8-3 4 8 6-20M44 40l8 20-8-3-4 8-6-20"/><path d="M27 26l4 4 7-8"/></svg>
  <h3>Marketing Qualified Leads (MQL)</h3>
  <p>A Marketing Qualified Lead (MQL) is a prospect that has expressed an interest in what your brand has to offer. An MQL has taken…</p>
  <a>READ MORE</a>
</div>
<div class="abs card" style="left:458px;top:1640px">
  <svg width="64" height="66" viewBox="0 0 64 66" fill="none" stroke="#c0282d" stroke-width="2"><circle cx="32" cy="10" r="5"/><path d="M32 15v8M16 24l10 8M48 24l-10 8"/><circle cx="14" cy="22" r="3"/><circle cx="50" cy="22" r="3"/><circle cx="18" cy="42" r="6"/><circle cx="32" cy="38" r="6"/><circle cx="46" cy="42" r="6"/><path d="M6 62c0-8 5-12 12-12s12 4 12 12M20 58c0-8 5-12 12-12s12 4 12 12M34 62c0-8 5-12 12-12s12 4 12 12"/></svg>
  <h3>Account Based Marketing Leads (ABM)</h3>
  <p>ABM is a strategy that directs marketing resources to engaging a specific set of target accounts. Instead of casting a wide.</p>
  <a>READ MORE</a>
</div>
<div class="abs card" style="left:764px;top:1640px">
  <svg width="64" height="66" viewBox="0 0 64 66" fill="none" stroke="#c0282d" stroke-width="2"><rect x="4" y="44" width="10" height="18"/><rect x="20" y="36" width="10" height="26"/><rect x="36" y="28" width="10" height="34"/><rect x="52" y="18" width="10" height="44"/><path d="M4 34 22 16l8 8L46 6M38 6h8v8"/></svg>
  <h3>Sales Qualified Lead<br>/ BANT</h3>
  <p>An SQL lead or a BANT lead is a type of lead that expressed a specific interest in a product and service that you have to offer…</p>
  <a>READ MORE</a>
</div>

<!-- QA Technology -->
<div class="abs" style="left:150px;top:2130px;width:409px;height:478px;background:linear-gradient(150deg,#1c2230,#0e1118 55%,#23303a)" role="img" aria-label="Close-up of colourful program code on a dark screen"></div>
<h2 class="abs serif h2" style="left:611px;top:2148px">QA Technology</h2>
<p class="abs para" style="left:611px;top:2225px;width:440px">Prospero is a proprietary lead verification platform from Brightfold Reach that aims to sift out invalid leads with questionable or erroneous data. The platform is designed to equip sales teams with accurate, high-quality records in order to improve lead generation, accelerate pipeline and increase revenue.</p>
<p class="abs para" style="left:611px;top:2411px;width:440px">Prospero is positioned to quickly identify, validate, and improve lead quality at the point-of-entry by filtering out all leads that do not match required filters, such as job title, company size, etc.</p>
<div class="abs btn btn-blue" style="left:611px;top:2520px">READ MORE</div>

<!-- Intent Data -->
<h2 class="abs serif h2" style="left:148px;top:2713px">Intent Data</h2>
<p class="abs para" style="left:148px;top:2791px;width:440px">Our relationships with the world's most important technology &amp; business decisions-makers generate a perpetual stream of global data. With access to 35 million individuals and a global behavioural data stream that is authenticated, timely and contextually relevant, we have one of the industry's most powerful signals of buyer intent and can fuel your demand-generation marketing strategies globally.</p>
<p class="abs para" style="left:148px;top:3003px;width:440px">We support our Intent targeting capabilities by partnering with a number of third party intent providers</p>
<div class="abs btn btn-blue" style="left:150px;top:3085px">READ MORE</div>
<div class="abs" style="left:640px;top:2695px;width:409px;height:479px;background:linear-gradient(160deg,#e9edf2,#c9d1da 55%,#8e98a4)" role="img" aria-label="Hand holding a smartphone showing a weather and analytics dashboard in an office"></div>

<!-- Testimonials -->
<h2 class="abs serif" style="left:0;top:3255px;width:1200px;text-align:center;font-size:40px">Client Testimonials</h2>
<div class="abs" style="left:544px;top:3351px;width:112px;height:112px;border-radius:50%;background:linear-gradient(160deg,#d8d8d8,#8a8a8a)" role="img" aria-label="Portrait of the client"></div>
<div class="abs quote-name">Lorem Ipsum is simply</div>
<p class="abs quote">Lorem Ipsum is simply dummy text of the printing and typesetting industry. Lorem Ipsum has been the industry's standard dummy text ever since the 1500s, when an unknown printer took a galley of type and scrambled it to make a type specimen book. It has survived not only five centuries, but also the leap into electronic typesetting, remaining essentially unchanged.</p>
<svg class="abs" style="left:184px;top:3600px" width="16" height="28" viewBox="0 0 16 28" fill="none" stroke="#333" stroke-width="2"><path d="M13 2 3 14l10 12"/></svg>
<svg class="abs" style="left:1004px;top:3600px" width="16" height="28" viewBox="0 0 16 28" fill="none" stroke="#333" stroke-width="2"><path d="M3 2l10 12L3 26"/></svg>

<!-- Footer -->
<footer class="abs footer"></footer>
<div class="abs contact" style="left:113px;top:3850px">
  <div class="ic"><svg width="20" height="26" viewBox="0 0 20 26"><path d="M10 1a9 9 0 0 0-9 9c0 7 9 15 9 15s9-8 9-15a9 9 0 0 0-9-9z" fill="#c0282d"/><circle cx="10" cy="10" r="3.3" fill="#fff"/></svg></div>
  <div><small>ADDRESS</small><b style="font-size:14px;line-height:22px;margin-top:8px">18 Harbour Lane, Suite 4<br>London, EC1A 9ZZ</b></div>
</div>
<div class="abs contact" style="left:467px;top:3854px">
  <div class="ic"><svg width="22" height="22" viewBox="0 0 22 22"><path d="M5 1l4 5-2 3c1 3 3 5 6 6l3-2 5 4-2 4C10 21 1 12 1 3z" fill="#c0282d"/></svg></div>
  <div><small style="font-size:12px">PHONE NUMBER</small><b style="font-size:22px;letter-spacing:1px;margin-top:2px">020-555-0148</b></div>
</div>
<div class="abs contact" style="left:762px;top:3854px">
  <div class="ic"><svg width="22" height="16" viewBox="0 0 22 16"><rect x="0" y="0" width="22" height="16" rx="2" fill="#c0282d"/><path d="M1 2l10 7 10-7" fill="none" stroke="#fff" stroke-width="1.6"/></svg></div>
  <div><small style="font-size:12px">EMAIL ADDRESS</small><b style="font-size:17px;margin-top:4px">info@brightfoldreach-example.com</b></div>
</div>
<nav class="abs foot-nav"><span>Home</span><span>About Us</span><span>Our Services</span><span>Prospero &amp; QA Technology</span><span>Intent Data</span><span>Testimonials</span><span>Contact Us</span></nav>
<div class="abs copy">Copyright 2020 Brightfoldreach-example.com</div>
<div class="abs social" aria-label="Social links"><span></span><span></span><span></span><span></span><span></span></div>

</body>
</html>
```